Peer-to-peer Car Rental Business needs a business card design

We need a business card design for a new company based in Melbourne, Australia called "Motorvale". We enable car owners to earny money by renting out their car to others in the community/neighbourhood when their not using it.
We would like to see designs that use the colour/s blue and/or orange.
The design should communicate young, modern, fun etc.
The themes to use should be community/neighbourhood, cars, parking, airports, car rental, sharing.

Target Market(s)

Young adults aged 20-35, travellers, environmentally conscious, cost conscious.

Industry/Entity Type

Business

Requirements
Must have
• Must have fields for persons name, title, mobile number, email company website.

```html
<!DOCTYPE html>
<html lang="en">
<head>
<meta charset="utf-8">
<title>Motorvale – Business Card</title>
<link href="https://fonts.googleapis.com/css2?family=Exo+2:wght@400;500&display=swap" rel="stylesheet">
<style>
  :root {
    --backdrop: #e6e6e4;
    --card: #ffffff;
    --brand-blue: #2f5ca6;
    --panel-blue: #1f4a8a;
    --panel-edge: #a9aaad;
    --ink: #1e1e22;
    --icon: #3a3f98;
    --on-panel: #ffffff;
  }
  * { margin: 0; padding: 0; box-sizing: border-box; }
  html, body {
    width: 1200px; height: 899px; overflow: hidden;
    background: var(--backdrop);
    font-family: "Exo 2", sans-serif;
  }
  .card {
    position: absolute; left: 100px; top: 164px;
    width: 1000px; height: 571px;
    background: var(--card);
    box-shadow: 0 6px 24px rgba(0,0,0,0.18);
    overflow: hidden;
  }
  .card__panel { position: absolute; inset: 0; width: 1000px; height: 571px; }
  .brand-name {
    position: absolute; left: 70px; top: 120px;
    font-size: 118px; font-weight: 400; letter-spacing: -1px;
    color: var(--brand-blue); line-height: 1;
  }
  .holder {
    position: absolute; right: 42px; top: 258px;
    text-align: right; color: var(--on-panel);
  }
  .holder__name { font-size: 30px; font-weight: 500; letter-spacing: 1px; }
  .holder__title { font-size: 22px; letter-spacing: 1.5px; margin-top: 2px; }
  .address {
    position: absolute; left: 72px; top: 330px;
    font-size: 22px; line-height: 1.35; color: var(--ink); letter-spacing: 0.5px;
  }
  .contacts {
    position: absolute; left: 74px; top: 410px;
    list-style: none; font-size: 21px; color: var(--ink); letter-spacing: 0.8px;
  }
  .contacts__item { display: flex; align-items: center; gap: 12px; height: 30px; }
  .contacts__icon { width: 20px; height: 20px; fill: var(--icon); flex: none; }
</style>
</head>
<body>
  <section class="card" aria-label="Motorvale business card">
    <svg class="card__panel" viewBox="0 0 1000 571" aria-hidden="true">
      <path d="M708 0 Q625 300 748 571 L1000 571 L1000 0 Z" fill="var(--panel-edge)"/>
      <path d="M720 0 Q638 300 762 571 L1000 571 L1000 0 Z" fill="var(--panel-blue)"/>
    </svg>

    <div class="brand-name">Motorvale</div>

    <div class="holder">
      <div class="holder__name">DANIEL HARPER</div>
      <div class="holder__title">FINANCIAL ADVISOR</div>
    </div>

    <address class="address" style="font-style:normal">
      041,12th floor,Park Crest<br>Road VIC
    </address>

    <ul class="contacts">
      <li class="contacts__item">
        <svg class="contacts__icon" viewBox="0 0 20 20"><path d="M5 2l3 4-2 2c1 2.5 3.5 5 6 6l2-2 4 3-2 3C9 18 2 11 2 4z"/></svg>
        012 345 6789
      </li>
      <li class="contacts__item">
        <svg class="contacts__icon" viewBox="0 0 20 20"><path d="M6 1h8a1 1 0 0 1 1 1v16a1 1 0 0 1-1 1H6a1 1 0 0 1-1-1V2a1 1 0 0 1 1-1zm1 2v12h6V3zm3 13.2a1 1 0 1 0 0 2 1 1 0 0 0 0-2z"/></svg>
        012 345 6789
      </li>
      <li class="contacts__item">
        <svg class="contacts__icon" viewBox="0 0 20 20"><path d="M6 2h7l3 3v4H6zM3 9h14a1 1 0 0 1 1 1v8H2v-8a1 1 0 0 1 1-1zm3 3v2h2v-2zm4 0v2h2v-2zm4 0v2h2v-2z"/></svg>
        012 345 6789
      </li>
      <li class="contacts__item">
        <svg class="contacts__icon" viewBox="0 0 20 20"><path d="M1 4h18v12H1zm2 2v.5l7 5 7-5V6l-7 5z"/></svg>
        urname@email.com
      </li>
      <li class="contacts__item">
        <svg class="contacts__icon" viewBox="0 0 20 20"><path d="M10 1a9 9 0 1 0 0 18 9 9 0 0 0 0-18zm0 2c1 1.2 1.8 3 2 5H8c.2-2 1-3.8 2-5zM3.1 8h3c.1-1.8.6-3.3 1.3-4.5A7 7 0 0 0 3.1 8zm9.5-4.5c.7 1.2 1.2 2.7 1.3 4.5h3a7 7 0 0 0-4.3-4.5zM3.1 12a7 7 0 0 0 4.3 4.5c-.7-1.2-1.2-2.7-1.3-4.5zm5 0c.2 2 1 3.8 2 5 1-1.2 1.8-3 2-5zm5.8 0c-.1 1.8-.6 3.3-1.3 4.5a7 7 0 0 0 4.3-4.5zM3 10h14"/></svg>
        www.urwebsitename.com
      </li>
    </ul>
  </section>
</body>
</html>
```